Optimization existing Business Card

I need a revision of the business card, incl. Logo Design. I am a freelancer and have my headquarters in Berlin. I develop business consulting solutions for banks, insurance and StartUp Companies. I want a simple design of the business card. The final design should professionalism and commitment and openness to communicate. I'm open minded in addition to optimizing the existing logo / business card as well on a new idea / proposal for the logo. Idea would be for example the logo of this page: http://varlow-strategic.consulting.

Target Market(s)

Consulting, Banking, Investment Banking

Industry/Entity Type

Business

Contact Information for Business Card

siehe Anhang (please take a look into the attachments, important)

Font styles to use
Sans Serif

Requirements
Must have
• Please look at my specifications exactly !! (Please see my specifications), CEO Founder not
Should not have
• No gradient !! (No overarching color gradient)

```html
<!DOCTYPE html>
<html lang="en">
<head>
<meta charset="utf-8">
<title>Varlow Consulting – Business Card</title>
<link rel="stylesheet" href="https://fonts.googleapis.com/css2?family=Arimo:wght@400;700&display=swap">
<style>
  :root {
    --backdrop: #707070;
    --paper: #e9e9e9;
    --brand-blue: #4560a6;
    --accent-blue: #1f6fc0;
    --ink: #111111;
    --contact-ink: #4a1a1a;
    --divider: #8a8a8a;
    --band-text: #ffffff;
  }
  * { box-sizing: border-box; margin: 0; padding: 0; }
  html, body { width: 1200px; height: 1200px; overflow: hidden; }
  body {
    background: var(--backdrop);
    font-family: "Arimo", Arial, sans-serif;
    position: relative;
  }
  .card {
    position: absolute;
    top: 440px;
    width: 500px;
    height: 300px;
    background: var(--paper);
    box-shadow: 0 4px 12px rgba(0,0,0,0.35);
    overflow: hidden;
  }
  .card--front { left: 75px; }
  .card--back { left: 625px; }

  .wordmark {
    display: flex;
    align-items: center;
    gap: 8px;
    color: var(--brand-blue);
    font-weight: 700;
    white-space: nowrap;
  }
  .wordmark__dot {
    width: 14px; height: 14px;
    border-radius: 50%;
    background: var(--brand-blue);
    flex: none;
  }
  .card--front .wordmark {
    position: absolute;
    left: 22px; top: 108px;
    font-size: 24px;
  }
  .card--back .wordmark {
    position: absolute;
    left: 0; right: 0; top: 0; bottom: 0;
    justify-content: center;
    font-size: 32px;
  }
  .card--back .wordmark__dot { width: 18px; height: 18px; }

  .divider {
    position: absolute;
    left: 250px; top: 20px;
    width: 1px; height: 210px;
    background: var(--divider);
  }
  .identity {
    position: absolute;
    left: 272px; top: 58px;
  }
  .identity__name {
    font-size: 22px;
    color: var(--ink);
    font-weight: 400;
  }
  .identity__role {
    font-size: 13.5px;
    color: var(--accent-blue);
    margin-top: 4px;
  }
  .contacts {
    position: absolute;
    left: 272px; top: 160px;
    list-style: none;
  }
  .contacts__item {
    display: flex;
    align-items: center;
    gap: 6px;
    font-size: 15px;
    color: var(--contact-ink);
    line-height: 22px;
    white-space: nowrap;
  }
  .contacts__icon {
    width: 12px; height: 12px;
    flex: none;
  }
  .address-band {
    position: absolute;
    left: 0; right: 0; bottom: 0;
    height: 56px;
    background: var(--brand-blue);
    color: var(--band-text);
    font-size: 15px;
    display: flex;
    align-items: center;
    justify-content: center;
  }
</style>
</head>
<body>
  <section class="card card--front" aria-label="Business card front">
    <div class="wordmark"><span class="wordmark__dot"></span>varlow consulting</div>
    <div class="divider"></div>
    <div class="identity">
      <h1 class="identity__name">Mara Lindqvist</h1>
      <p class="identity__role">Founder, Management Consultant</p>
    </div>
    <ul class="contacts">
      <li class="contacts__item">
        <svg class="contacts__icon" viewBox="0 0 12 12" aria-hidden="true"><rect width="12" height="12" rx="1.5" fill="#1f6fc0"/><path d="M4 2.5 L5.2 4.2 L4.5 5 Q5.3 6.8 7 7.5 L7.8 6.8 L9.5 8 L8.6 9.4 Q5 9 2.6 3.4 Z" fill="#fff"/></svg>
        +49 (0) 30555018420
      </li>
      <li class="contacts__item">
        <svg class="contacts__icon" viewBox="0 0 12 12" aria-hidden="true"><rect width="12" height="12" rx="1.5" fill="#1f6fc0"/><rect x="4" y="2" width="4" height="8" rx="0.8" fill="#fff"/><rect x="4.8" y="3" width="2.4" height="4.5" fill="#1f6fc0"/></svg>
        +49 (0) 15550193274
      </li>
      <li class="contacts__item">
        <svg class="contacts__icon" viewBox="0 0 12 12" aria-hidden="true"><rect width="12" height="12" rx="1.5" fill="#1f6fc0"/><rect x="2.5" y="3.5" width="7" height="5" fill="#fff"/><path d="M2.5 3.5 L6 6.3 L9.5 3.5" fill="none" stroke="#1f6fc0" stroke-width="0.8"/></svg>
        ml@varlow-consulting.de
      </li>
    </ul>
    <div class="address-band">Lindenallee 45, 10115 Berlin, Germany</div>
  </section>

  <section class="card card--back" aria-label="Business card back">
    <div class="wordmark"><span class="wordmark__dot"></span>varlow consulting</div>
  </section>
</body>
</html>
```